30th Anniversary Poster

Need a 2ft (Wide) X 3ft (Tall) Poster design for a 30th anniversary party that will be used in .  Need the get the logo to be the theme colors (gold).  Overall theme is elegance with gold and black being the main colors.  The background should be black.  Silver can be used as an accent color.  I need the sign to say Welcome and 30th Anniversary.  I need all text to be editable and fonts easily available.
A feel similar to images in this search is pretty close.
https://www.brivolsearch.example/find?tk=9b2e71c04d8a5f36&ref=7QXPLMZ_wnTR441TR441&sid=KQPWRTzNmv8LdHysXaPq2GbTc3RrxW:2841099670862&q=gala+event+poster&mode=2&flt=ZRTQmB1Bb5tjXe43Ry6qFxSkVe9cPKgmzCSTTT6OS4wLVQ8yXt7ZdHyUg39F7Nalr4MkiDuS42Z9kOnPyrk1jfnd0Bp8RwhSbbCqXfe7YdWkpPmX1zYXMS6W2olZPTbejwdwlW27yNbCepq98SaKnGcdJvHpE1Ddb2Y4UbrTBkS6SVtXdTDVBq1XCUc7-1DVXDpXpV-Tfk8Xk_MwspEsTvLvWAqp9-IBcqmUh_NGXYB&ax=Y&ib=3&vx=3bqVLxj3ttrkBzYkNeGqUJQV&bw=1728&bh=840&pr=2

```html
<!DOCTYPE html>
<html lang="en">
<head>
<meta charset="utf-8">
<title>Marlow Systems – 30th Anniversary Welcome Poster</title>
<link rel="stylesheet" href="https://fonts.googleapis.com/css2?family=Anton&family=Cinzel:wght@400;600&display=swap">
<style>
  :root {
    --black: #000000;
    --night: #0b0a08;
    --gold: #d9a520;
    --gold-light: #f7d96a;
    --gold-deep: #9a6a0c;
    --gold-glow: rgba(240, 170, 60, 0.55);
    --silver: #c9c9c9;
  }
  * { margin: 0; padding: 0; box-sizing: border-box; }
  html, body {
    width: 808px;
    height: 1200px;
    overflow: hidden;
    background: var(--black);
  }
  .poster {
    position: relative;
    width: 808px;
    height: 1200px;
    overflow: hidden;
    background: radial-gradient(ellipse 70% 45% at 45% 30%, #17130b 0%, var(--night) 55%, var(--black) 100%);
  }
  .decor { position: absolute; pointer-events: none; }
  .decor--dust {
    left: 60px; top: 0; width: 700px; height: 760px;
    background:
      radial-gradient(ellipse 45% 20% at 55% 8%, rgba(190, 140, 50, 0.28), transparent 70%),
      radial-gradient(ellipse 30% 25% at 70% 62%, rgba(200, 150, 60, 0.22), transparent 70%);
  }
  .decor--coins {
    right: 0; top: 0; width: 190px; height: 170px;
    background: radial-gradient(circle at 80% 25%, rgba(235, 175, 60, 0.75), rgba(160, 90, 20, 0.3) 45%, transparent 72%);
  }
  .decor--swoosh-right {
    right: 0; top: 300px; width: 360px; height: 300px;
    background: radial-gradient(ellipse 60% 30% at 70% 40%, rgba(230, 150, 50, 0.45), transparent 70%);
    transform: rotate(-25deg);
  }
  .decor--flare {
    left: 480px; top: 470px; width: 120px; height: 120px;
    background: radial-gradient(circle, rgba(255, 235, 200, 0.9), var(--gold-glow) 25%, transparent 70%);
  }
  .decor--streak-left {
    left: 0; top: 760px; width: 260px; height: 110px;
    background: radial-gradient(ellipse 60% 30% at 30% 55%, rgba(230, 140, 40, 0.5), transparent 72%);
  }
  .decor--waves {
    left: 0; bottom: 0; width: 808px; height: 110px;
    background: linear-gradient(180deg, transparent 0%, rgba(150, 100, 30, 0.45) 45%, rgba(210, 160, 70, 0.6) 75%, rgba(90, 60, 20, 0.5) 100%);
  }
  .frame-lines {
    position: absolute; left: 0; top: 0;
  }
  .brand {
    position: absolute;
    left: 0; top: 196px; width: 808px;
    display: flex; align-items: center; justify-content: center; gap: 16px;
  }
  .brand__dot {
    width: 22px; height: 22px; border-radius: 50%;
    background: var(--gold);
  }
  .brand__name {
    font-family: "Cinzel", serif;
    font-weight: 600;
    font-size: 40px;
    letter-spacing: 3px;
    color: var(--gold);
  }
  .headline {
    position: absolute; left: 0; top: 0;
  }
  .headline text { font-family: "Cinzel", serif; }
  .headline .headline__number { font-family: "Anton", sans-serif; }
</style>
</head>
<body>
<main class="poster">
  <div class="decor decor--dust" role="img" aria-label="Fine gold glitter dust drifting across the black background"></div>
  <div class="decor decor--coins" role="img" aria-label="Scattered gold coins glowing in the top right corner"></div>
  <div class="decor decor--swoosh-right" role="img" aria-label="Flowing gold light ribbon sweeping in from the right"></div>
  <div class="decor decor--flare" role="img" aria-label="Bright lens flare sparkle"></div>
  <div class="decor decor--streak-left" role="img" aria-label="Gold light streak with bokeh on the left edge"></div>
  <div class="decor decor--waves" role="img" aria-label="Layered gold silk waves along the bottom edge"></div>

  <svg class="frame-lines" width="808" height="1200" viewBox="0 0 808 1200" aria-hidden="true">
    <path d="M0 935 L120 1200" stroke="var(--gold-light)" stroke-opacity="0.55" stroke-width="1.5" fill="none"/>
    <path d="M808 935 L690 1200" stroke="var(--gold-light)" stroke-opacity="0.55" stroke-width="1.5" fill="none"/>
  </svg>

  <header class="brand">
    <span class="brand__dot"></span>
    <span class="brand__name">MARLOW SYSTEMS</span>
  </header>

  <svg class="headline" width="808" height="1200" viewBox="0 0 808 1200">
    <defs>
      <linearGradient id="goldText" x1="0" y1="0" x2="0" y2="1">
        <stop offset="0" stop-color="var(--gold-light)"/>
        <stop offset="0.55" stop-color="var(--gold)"/>
        <stop offset="1" stop-color="var(--gold-deep)"/>
      </linearGradient>
      <linearGradient id="goldNumber" x1="0" y1="0" x2="1" y2="1">
        <stop offset="0" stop-color="#f5d56a"/>
        <stop offset="0.5" stop-color="#e3b534"/>
        <stop offset="1" stop-color="#b8861a"/>
      </linearGradient>
    </defs>
    <text class="headline__welcome" x="138" y="443" font-size="64" textLength="458" lengthAdjust="spacing" fill="url(#goldText)">WELCOME</text>
    <text class="headline__number" x="193" y="831" font-size="370" textLength="343" lengthAdjust="spacingAndGlyphs" fill="url(#goldNumber)">30</text>
    <text class="headline__suffix" x="542" y="831" font-size="62" textLength="108" lengthAdjust="spacing" fill="url(#goldText)">TH</text>
    <text class="headline__anniversary" x="106" y="933" font-size="68" textLength="586" lengthAdjust="spacing" fill="url(#goldText)">ANNIVERSARY</text>
  </svg>
</main>
</body>
</html>
```